Company brochure

I would like to redesign our existing brochure.
It shall be trifold brochure with more modern and better appealing design than the old one. I am uploading the old one. The new design shall have all all information repeated from old brochure. It could be more or less pictures. I will provide more pictures if required. The keep text is important, the font shall be more modern. Brochure size shall be trifoldt US Legal size paper 8.5" x 14". I will provide all pitures, logos etc in a original format after design concept will be established or before on request.

Industry/Entity Type

It Company

Font styles to use
Other font styles liked:
• calibri

Colors
0555a3
3176b5
85abd2
0692cd
33a6d7
85cae6
1ab09a
33b8a4
87cfc6

Requirements
Nice to have
• I need all information from existing brochure such as text, customer logos, professional assos. logos to be shown in a new one. Picture could be added more.
Should not have
• No changes allowed to company letterhead. Only slight modifications allowed to company logo

```html
<!DOCTYPE html>
<html lang="en">
<head>
<meta charset="utf-8">
<title>Coldline Refrigeration &amp; Air Conditioning – Trifold Brochure</title>
<link rel="stylesheet" href="https://fonts.googleapis.com/css2?family=Oswald:wght@300;400;700&family=Open+Sans:wght@400;600&display=swap">
<style>
  :root {
    --navy: #0555a3;
    --blue: #3176b5;
    --sky: #85abd2;
    --cyan: #0692cd;
    --cyan-soft: #33a6d7;
    --ice: #85cae6;
    --teal: #1ab09a;
    --teal-mid: #33b8a4;
    --teal-soft: #87cfc6;
    --ink: #1b2233;
    --stage: #2a2a2c;
    --paper: #ffffff;
  }
  * { box-sizing: border-box; margin: 0; padding: 0; }
  html, body { width: 756px; height: 1200px; overflow: hidden; background: var(--stage); }
  .canvas { position: relative; width: 756px; height: 1200px; }

  .spread {
    position: absolute; left: 20px; top: 383px; width: 716px; height: 433px;
    display: flex; box-shadow: 0 10px 30px rgba(0,0,0,.5); overflow: hidden;
  }
  .panel { position: relative; height: 100%; overflow: hidden; }
  .panel--services { width: 239px; background: linear-gradient(165deg, var(--navy) 0%, var(--blue) 45%, var(--cyan) 100%); color: #fff; }
  .panel--contact { width: 238px; background: var(--paper); }
  .panel--cover { width: 239px; background: var(--paper); }

  .shape-layer { position: absolute; inset: 0; width: 100%; height: 100%; }

  /* Services panel */
  .service { position: absolute; left: 0; right: 14px; }
  .service__title {
    position: relative; font-family: "Oswald", sans-serif; font-weight: 300; font-size: 12.5px;
    line-height: 1.35; padding-left: 19px; border-bottom: 0.6px solid rgba(255,255,255,.55); padding-bottom: 2px;
  }
  .service__title::before {
    content: ""; position: absolute; left: 0; top: 3px; width: 5px; height: 13px; background: var(--ice);
  }
  .service__text {
    font-family: "Open Sans", sans-serif; font-size: 6.4px; line-height: 1.48; text-align: justify;
    padding: 6px 0 0 19px; color: #eaf4fb;
  }
  .service--refrigeration { top: 33px; }
  .service--hvac { top: 114px; }
  .service--construction { top: 199px; }
  .service--construction .service__title { padding-bottom: 1px; }
  .photo--plant {
    position: absolute; left: 19px; top: 225px; width: 200px; height: 81px;
    border: 2px solid var(--ice);
    background: linear-gradient(120deg, #c9ced3 0%, #e8eaec 35%, #2f6d6b 60%, #1f4d52 80%, #9aa3a8 100%);
  }
  .construction-text {
    position: absolute; left: 19px; right: 14px; top: 315px;
    font-family: "Open Sans", sans-serif; font-size: 6.4px; line-height: 1.52; text-align: justify; color: #eaf4fb;
  }

  /* Contact panel */
  .photo--warehouse {
    position: absolute; left: 0; top: 0; width: 238px; height: 150px;
    background: linear-gradient(100deg, #d7dbdf 0%, #f2f3f4 30%, #c7ccd2 55%, #2a4c86 72%, #e6e8ea 85%, #bfc4ca 100%);
  }
  .contact { position: absolute; left: 0; right: 0; top: 190px; text-align: center; color: var(--ink); }
  .brand {
    font-family: "Oswald", sans-serif; font-weight: 700; color: var(--navy);
    text-transform: uppercase; letter-spacing: -0.2px; line-height: 1.05; text-align: left;
  }
  .brand--contact { display: inline-flex; align-items: center; gap: 7px; font-size: 14px; }
  .brand__dot { width: 14px; height: 14px; border-radius: 50%; background: var(--cyan); flex: none; }
  .contact__lines { margin-top: 13px; font-family: "Open Sans", sans-serif; font-size: 8.2px; line-height: 1.45; }
  .contact__gap { height: 6px; }
  .contact__license { font-weight: 600; }
  .memberships { position: absolute; left: 12px; right: 12px; top: 350px; display: flex; justify-content: space-between; align-items: center; }
  .badge { background: var(--sky); }
  .badge--store { width: 54px; height: 20px; background: linear-gradient(var(--navy) 0 50%, #c0392b 50% 100%); }
  .badge--society { width: 30px; height: 26px; clip-path: polygon(25% 0, 75% 0, 100% 50%, 75% 100%, 25% 100%, 0 50%); background: var(--cyan-soft); }
  .badge--association { width: 30px; height: 30px; border-radius: 50%; border: 3px solid var(--navy); background: #fff; }
  .badge--institute { width: 42px; height: 24px; border-radius: 50%; border: 2.5px solid var(--blue); background: #fff; }

  /* Cover panel */
  .cover__head { position: absolute; left: 0; right: 0; top: 0; height: 112px; background: linear-gradient(180deg, #fff 0%, #eef0f2 100%); }
  .brand--cover { position: absolute; left: 22px; top: 30px; display: flex; align-items: center; gap: 9px; font-size: 17px; }
  .brand--cover .brand__dot { width: 16px; height: 16px; }
  .cover__rule { position: absolute; left: 70px; right: 16px; top: 87px; height: 0; border-top: 1.4px solid var(--blue); }
  .cover__rule::after {
    content: ""; position: absolute; left: 50%; top: -4px; width: 6px; height: 6px; background: var(--blue);
    transform: translateX(-50%) rotate(45deg);
  }
  .cover__services {
    position: absolute; left: 0; right: 0; top: 112px; height: 68px;
    font-family: "Oswald", sans-serif; font-weight: 300; font-size: 8.4px; line-height: 1.6; color: #fff;
  }
  .cover__list { position: absolute; top: 18px; }
  .cover__list--left { left: 10px; }
  .cover__list--right { left: 139px; }
  .photo--rooftop {
    position: absolute; left: 0; top: 180px; width: 239px; height: 202px;
    background: linear-gradient(180deg, #8fb5d6 0%, #cfdbe4 18%, #3d5a3a 22%, #e9ebec 28%, #b8bec4 55%, #dfe2e5 100%);
  }
  .cover__url {
    position: absolute; left: 0; right: 0; top: 405px; text-align: center;
    font-family: "Oswald", sans-serif; font-weight: 300; font-size: 10px; letter-spacing: 2.6px; color: #fff;
  }
</style>
</head>
<body>
<div class="canvas">
  <main class="spread">

    <section class="panel panel--services">
      <div class="service service--refrigeration">
        <h2 class="service__title">Refrigeration Facilities Serviced</h2>
        <p class="service__text">Food processing, cold storages and distribution facilities, meat and poultry processing plants, bakeries, dairies, beverage bottling facilities, ice production, chemical plants, refineries and ice rinks.</p>
      </div>
      <div class="service service--hvac">
        <h2 class="service__title">Industrial &amp; Commercial HVAC<br>Facilities Serviced</h2>
        <p class="service__text">Production plant and manufacturing facilities, distribution and storage warehouses, office buildings, data centers, hospitals, colleges, shopping malls and country clubs.</p>
      </div>
      <div class="service service--construction">
        <h2 class="service__title">Construction</h2>
      </div>
      <div class="photo photo--plant" role="img" aria-label="Photo of an industrial refrigeration machine room with compressors and piping"></div>
      <p class="construction-text">Ammonia and freon refrigeration build-up systems. Refrigeration and HVAC equipment changeover. Freon packaged condensing units and chillers. Blast freezers, spiral and tunnel freezers. Computerized control, control and power wiring. Build-up glycol and water chillers. Air handlers and evaporators. Refrigeration, glycol, chill water and process piping. Certified X-ray quality welding. Carbon steel, stainless steel, copper, PVC and sanitary piping. Hot tapping available.</p>
      <svg class="shape-layer" viewBox="0 0 239 433" preserveAspectRatio="none" aria-hidden="true">
        <polygon points="0,410 239,410 239,433 0,433" fill="var(--teal-soft)" opacity=".55"/>
        <polygon points="0,388 52,433 0,433" fill="var(--teal-soft)"/>
        <polygon points="0,418 239,418 239,433 0,433" fill="var(--teal-mid)" opacity=".35"/>
      </svg>
    </section>

    <section class="panel panel--contact">
      <div class="photo photo--warehouse" role="img" aria-label="Photo of a cold storage warehouse interior with blue high-speed doors"></div>
      <svg class="shape-layer" viewBox="0 0 238 433" preserveAspectRatio="none" aria-hidden="true">
        <polygon points="0,140 74,140 62,150 0,150" fill="var(--teal-soft)"/>
        <polygon points="100,113 238,113 238,180 0,180 0,150 62,150" fill="var(--cyan)"/>
        <polygon points="130,113 238,113 238,180 60,180" fill="var(--navy)" opacity=".5"/>
        <polygon points="0,410 238,410 238,433 0,433" fill="var(--teal-soft)"/>
        <polygon points="0,422 238,418 238,433 0,433" fill="var(--teal-mid)" opacity=".45"/>
      </svg>
      <div class="contact">
        <div class="brand brand--contact"><span class="brand__dot"></span><span>Coldline Refrigeration<br>&amp; Air Conditioning</span></div>
        <div class="contact__lines">
          <p>4810 Harlow Avenue</p>
          <p>Eastbrook, CA 91840</p>
          <div class="contact__gap"></div>
          <p>555-201-4410</p>
          <p>555-201-4411</p>
          <p>www.coldlinerac.com</p>
          <p class="contact__license">Lic. # 481207</p>
        </div>
      </div>
      <div class="memberships">
        <span class="badge badge--store"></span>
        <span class="badge badge--society"></span>
        <span class="badge badge--association"></span>
        <span class="badge badge--institute"></span>
      </div>
    </section>

    <section class="panel panel--cover">
      <header class="cover__head">
        <h1 class="brand brand--cover"><span class="brand__dot"></span><span>Coldline Refrigeration<br>&amp; Air Conditioning</span></h1>
        <div class="cover__rule"></div>
      </header>
      <svg class="shape-layer" viewBox="0 0 239 433" preserveAspectRatio="none" aria-hidden="true">
        <polygon points="0,112 239,112 239,180 0,180" fill="var(--cyan)"/>
        <polygon points="0,112 150,112 120,180 0,180" fill="var(--navy)" opacity=".55"/>
        <polygon points="150,112 239,112 239,124 146,124" fill="var(--cyan-soft)"/>
      </svg>
      <div class="cover__services">
        <ul class="cover__list cover__list--left" style="list-style:none">
          <li>Industrial &amp; Commercial</li>
          <li>Ammonia &amp; Freon</li>
          <li>Service &amp; Maintenance</li>
        </ul>
        <ul class="cover__list cover__list--right" style="list-style:none">
          <li>Design &amp; Engineering</li>
          <li>Construction</li>
        </ul>
      </div>
      <div class="photo photo--rooftop" role="img" aria-label="Photo of insulated refrigeration piping runs on a commercial rooftop"></div>
      <svg class="shape-layer" viewBox="0 0 239 433" preserveAspectRatio="none" aria-hidden="true">
        <polygon points="0,380 239,372 239,390 0,398" fill="var(--teal-soft)"/>
        <polygon points="0,398 239,390 239,433 0,433" fill="var(--cyan)"/>
        <polygon points="0,410 239,404 239,433 0,433" fill="var(--navy)" opacity=".35"/>
      </svg>
      <p class="cover__url">www.coldlinerac.com</p>
    </section>

  </main>
</div>
</body>
</html>
```